Website Design for Employee Moral and Happiness Company

Looking for a clean website design that explains our features in a step by step manner so our visitors know exactly what our site does before logging in.

The site is called "Velquo". See logo design and video for a sample of style and an overview of what we do.

Target Market(s)

Business owners that are looking to retain employees.

Number of Pages Required

1 page

```html
<!DOCTYPE html>
<html lang="en">
<head>
<meta charset="utf-8">
<title>Velquo – Employee Happiness</title>
<link href="https://fonts.googleapis.com/css2?family=Arvo:wght@400;700&family=Open+Sans:wght@400;600;700&display=swap" rel="stylesheet">
<style>
:root{
  --orange:#ff6a00;
  --orange-deep:#e85500;
  --orange-soft:#ff9a4d;
  --navy:#1b2d4f;
  --navy-deep:#14233f;
  --dark:#2e2e2e;
  --ink:#1e1e1e;
  --text:#555;
  --peach:#fdeee6;
  --footer:#1b1b1b;
  --white:#fff;
}
*{box-sizing:border-box;margin:0;padding:0}
html,body{width:1200px;height:4736px;overflow:hidden}
body{font-family:"Open Sans",Arial,sans-serif;color:var(--text);background:var(--white);position:relative}
section,header,nav,footer{position:relative;width:1200px;overflow:hidden}
.abs{position:absolute}
h1,h2,h3,.slab{font-family:"Arvo",Georgia,serif;color:var(--ink)}
.btn{position:absolute;display:inline-block;background:var(--orange);color:#fff;font-weight:700;font-size:15px;border-radius:24px;padding:11px 24px;white-space:nowrap}
p{font-size:14px;line-height:24px}

/* top bar */
.topbar{height:48px;background:var(--orange)}
.topbar .navy-part{position:absolute;left:0;top:0;width:600px;height:48px;background:var(--navy);clip-path:polygon(0 0,100% 0,95% 100%,0 100%)}
.topbar .top-contact{position:absolute;left:160px;top:7px;display:flex;gap:14px;align-items:center;color:#fff;font-size:13px;line-height:16px;white-space:nowrap}
.ic-circle{width:26px;height:26px;border-radius:50%;background:var(--orange);display:flex;align-items:center;justify-content:center;flex:none}
.topbar .ask{position:absolute;left:812px;top:4px;width:230px;height:38px;border-radius:20px;background:#141414;display:flex;gap:14px;align-items:center;padding-left:12px;color:#fff;font-size:13px;line-height:16px;white-space:nowrap}

/* nav */
.nav{height:69px;background:#fff}
.logo{font-family:"Arvo",Georgia,serif;font-weight:700;font-size:42px;line-height:56px;color:var(--ink);position:absolute;left:160px;top:4px;letter-spacing:1px}
.menu{position:absolute;right:158px;top:24px;display:flex;gap:42px;font-size:14px;font-weight:600;color:var(--ink);white-space:nowrap}
.menu .active{color:var(--orange)}

/* hero */
.hero{height:548px}
.hero-photo{position:absolute;inset:0;background:linear-gradient(120deg,#f46a10 0%,#ff7b22 40%,#e85a00 100%)}
.hero h1{position:absolute;left:157px;top:298px;color:#fff;font-size:42px;line-height:50px}
.hero h1 .dash{display:inline-block;width:46px;height:2px;background:#fff;vertical-align:middle;margin-right:8px}
.arrow-btn{position:absolute;top:420px;width:32px;height:32px;border-radius:50%;background:#fff;display:flex;align-items:center;justify-content:center}
.arrow-btn.ghost{background:transparent;border:2px solid #fff}

/* about */
.about{height:485px}
.dots{position:absolute;background-image:radial-gradient(circle,#222 2px,transparent 2.5px);background-size:17px 17px}
.about .ring{position:absolute;left:167px;top:52px;width:395px;height:395px;border-radius:50%;background:var(--orange)}
.about .photo{position:absolute;left:185px;top:37px;width:362px;height:362px;border-radius:50%;border:8px solid #fff;background:linear-gradient(135deg,#e8e6e3,#9b9793 60%,#4a4a4a)}
.about .bubble{position:absolute;left:472px;top:56px;width:56px;height:56px;border-radius:50%;background:var(--orange)}
.about h2{position:absolute;left:643px;top:86px;font-size:40px}
.about .copy{position:absolute;left:643px;top:150px;width:400px}
.about .copy p{margin-bottom:10px}

/* schedule */
.schedule{height:490px;background:var(--navy)}
.schedule .photo-wash{position:absolute;inset:0;background:linear-gradient(90deg,rgba(20,35,63,.9),rgba(40,60,96,.85))}
.schedule h2{position:absolute;left:157px;top:128px;color:#fff;font-size:40px;line-height:57px}
.schedule p{position:absolute;left:157px;top:246px;width:360px;color:#fff}
.schedule .btn{left:157px;top:312px}
.cal-bracket{position:absolute;left:575px;top:100px;width:120px;height:130px;border-left:12px solid var(--orange);border-top:12px solid var(--orange)}
.cal{position:absolute;left:588px;top:114px;width:436px;height:313px;background:#fff;padding:10px 10px 12px;box-shadow:0 6px 16px rgba(0,0,0,.3)}
.cal table{width:100%;height:100%;border-collapse:collapse;border:2px solid #111}
.cal th.title{font-family:Arial,sans-serif;font-weight:400;font-size:42px;line-height:40px;color:#111;border-bottom:2px solid #111}
.cal th.day{font-size:11px;font-weight:400;color:#111;border:1px solid #111;height:14px;background:#eee}
.cal td{border:1px solid #111;font-size:10px;color:#111;text-align:right;vertical-align:top;padding:1px 3px;width:14.28%}
.cal td.mute{color:#aaa}
.cal-plus{position:absolute;left:993px;top:62px;width:48px;height:48px;border-radius:50%;background:var(--orange);color:#fff;font-size:30px;line-height:46px;text-align:center}

/* why */
.why{height:562px;background:#fff}
.why .blob{position:absolute;background:var(--peach);border-radius:50%}
.why h2{position:absolute;left:0;width:1200px;text-align:center;top:70px;font-size:40px}
.feature{position:absolute;width:283px;height:117px}
.feature .frame{position:absolute;left:8px;top:0;width:255px;height:117px;border:3px solid var(--orange)}
.feature .pill{position:absolute;left:0;top:4px;width:283px;height:110px;background:var(--dark);border-radius:55px}
.feature .label{position:absolute;left:30px;top:26px;width:140px;text-align:right;color:#fff}
.feature .label b{display:block;font-family:"Arvo",Georgia,serif;font-size:17px;margin-bottom:3px}
.feature .label span{font-size:13px;line-height:18px;display:block}
.feature .icon{position:absolute;right:14px;top:17px;width:84px;height:84px;border-radius:50%;background:#fff;display:flex;align-items:center;justify-content:center}
.why .center-ring{position:absolute;left:453px;top:176px;width:297px;height:297px;border-radius:50%;border:3px solid var(--orange)}
.why .center{position:absolute;left:467px;top:190px;width:269px;height:269px;border-radius:50%;background:var(--orange)}

/* how */
.how{height:430px;background:#333}
.how .wash{position:absolute;inset:0;background:linear-gradient(90deg,#2c2c2c,#3d3d3d 60%,#2a2a2a)}
.how .orange-back{position:absolute;left:162px;top:73px;width:446px;height:292px;background:var(--orange)}
.how .orange-top{position:absolute;left:457px;top:38px;width:165px;height:70px;background:var(--orange)}
.how .video{position:absolute;left:180px;top:62px;width:425px;height:281px;border:4px solid #fff;background:linear-gradient(135deg,#b9b2aa,#7a6d62 55%,#4b433c)}
.how .play{position:absolute;left:343px;top:153px;width:100px;height:100px;border-radius:50%;background:rgba(255,255,255,.8);display:flex;align-items:center;justify-content:center}
.how h2{position:absolute;left:651px;top:98px;color:#fff;font-size:40px}
.how p{position:absolute;left:651px;top:160px;width:400px;color:#fff}
.how .btn{left:651px;top:278px}

/* events */
.events{height:658px}
.events h2{position:absolute;left:0;width:1200px;text-align:center;top:50px;font-size:40px}
.event-main{position:absolute;left:160px;top:119px;width:424px;height:281px;border:4px solid #fff;box-shadow:0 2px 8px rgba(0,0,0,.3);background:linear-gradient(135deg,#eceae6,#c9c3bc 55%,#8e8680)}
.date{font-family:"Arvo",Georgia,serif;font-weight:700;font-size:14px;color:var(--ink);display:flex;align-items:center;gap:6px}
.event-title{font-family:"Arvo",Georgia,serif;font-weight:700;font-size:20px;line-height:28px;color:var(--ink)}
.event-side{position:absolute;left:610px;width:432px;height:121px}
.event-side .thumb{position:absolute;left:0;top:0;width:165px;height:121px;border:3px solid #fff;box-shadow:0 2px 6px rgba(0,0,0,.3)}
.event-side .info{position:absolute;left:180px;top:20px}
.events .btn{left:537px;top:560px;padding:11px 32px}

/* contact */
.contact-sec{height:500px;background:var(--orange)}
.contact-sec .wash{position:absolute;inset:0;background:linear-gradient(180deg,#ff6f0e,#f46500)}
.contact-sec h2{position:absolute;left:0;width:1200px;text-align:center;top:108px;color:#fff;font-size:40px}
.field{position:absolute;height:37px;background:#fff;border-radius:6px;font-size:12px;color:#333;padding:10px 18px}
.contact-sec .submit{left:537px;top:405px;background:var(--ink);padding:11px 22px}

/* testimonial */
.testi{height:501px}
.testi h2{position:absolute;left:0;width:1200px;text-align:center;top:55px;font-size:40px}
.quote{position:absolute;top:133px;width:283px}
.stars{display:flex;align-items:center;gap:4px}
.stars .line{flex:1;height:1px;background:#ccc;margin-left:8px}
.quote .mark{font-family:Georgia,serif;font-size:32px;color:#bbb;line-height:24px;margin-top:12px}
.quote p{font-size:14px;line-height:24px;color:#555}
.who{position:absolute;left:0;top:228px;width:283px;height:58px;background:var(--navy)}
.who .tri{position:absolute;left:0;top:0;width:70px;height:58px;background:var(--orange);clip-path:polygon(0 0,100% 50%,0 100%)}
.who .avatar{position:absolute;left:14px;top:6px;width:46px;height:46px;border-radius:50%;border:3px solid #fff;background:linear-gradient(135deg,#d9a37a,#8a5a3a)}
.who .name{position:absolute;left:100px;top:12px;color:#fff;font-size:13px;line-height:16px}
.pager{position:absolute;left:575px;top:443px;display:flex;gap:10px}
.pager i{width:10px;height:10px;border-radius:50%;border:1.5px solid #999}
.pager i.on{background:var(--orange);border-color:var(--orange)}

/* footer */
.footer{height:445px;background:var(--footer);color:#ddd}
.footer .col{position:absolute;top:0;height:290px;border-left:1px solid #555}
.footer h4{font-family:"Open Sans",Arial,sans-serif;font-style:italic;font-weight:400;font-size:16px;color:#fff;border-left:4px solid var(--orange);padding-left:18px;margin-left:-2px;margin-top:100px;line-height:22px}
.footer .logo{position:relative;left:auto;top:auto;color:#fff;font-size:38px;line-height:46px}
.footer .about-txt{font-size:13px;line-height:23px;margin-top:14px;width:240px}
.footer ul{list-style:none;margin:20px 0 0 50px;font-size:13px}
.footer li{display:flex;align-items:center;gap:18px;line-height:25px}
.footer .contact-list li{align-items:flex-start;line-height:18px;margin-bottom:20px;gap:16px}
.footer .social li{line-height:32px;gap:14px}
.sq{width:24px;height:24px;border-radius:50%;background:#8a8a8a;flex:none}
.footer .copy{position:absolute;left:0;width:1200px;top:370px;text-align:center;font-size:12px}
</style>
</head>
<body>

<header class="topbar">
  <div class="navy-part"></div>
  <div class="top-contact">
    <span class="ic-circle"><svg width="14" height="10" viewBox="0 0 14 10"><rect x=".5" y=".5" width="13" height="9" fill="none" stroke="#fff"/><path d="M.5 .5 7 6l6.5-5.5" fill="none" stroke="#fff"/></svg></span>
    <span>Get In Touch<br>info@velquo.com</span>
  </div>
  <div class="ask">
    <span class="ic-circle"><svg width="14" height="14" viewBox="0 0 24 24"><path fill="#fff" d="M6.6 10.8a15 15 0 0 0 6.6 6.6l2.2-2.2c.3-.3.7-.4 1-.2 1.1.4 2.3.6 3.6.6.6 0 1 .4 1 1V20c0 .6-.4 1-1 1A17 17 0 0 1 3 4c0-.6.4-1 1-1h3.5c.6 0 1 .4 1 1 0 1.3.2 2.5.6 3.6.1.3 0 .7-.2 1z"/></svg></span>
    <span>Have any questions?<br>555-014-2870</span>
  </div>
</header>

<nav class="nav">
  <div class="logo">velquo</div>
  <div class="menu"><span class="active">Home</span><span>About</span><span>Solution</span><span>Event</span><span>Contact Us</span></div>
</nav>

<section class="hero">
  <div class="hero-photo" role="img" aria-label="Smiling team celebrating in an office, tinted orange"></div>
  <h1>Increase<br><span class="dash"></span>Employee<br>Retention</h1>
  <span class="arrow-btn" style="left:961px"><svg width="12" height="12" viewBox="0 0 12 12"><path d="M8 1 3 6l5 5" fill="none" stroke="#222" stroke-width="2"/></svg></span>
  <span class="arrow-btn ghost" style="left:1008px"><svg width="12" height="12" viewBox="0 0 12 12"><path d="M4 1l5 5-5 5" fill="none" stroke="#fff" stroke-width="2"/></svg></span>
  <svg class="abs" style="left:0;top:440px" width="1200" height="108" viewBox="0 0 1200 108">
    <path d="M0 108 C300 60 700 20 1200 55 L1200 108 Z" fill="#fff"/>
    <path d="M0 108 C300 60 700 20 1200 55" fill="none" stroke="#15203a" stroke-width="6"/>
  </svg>
</section>

<section class="about">
  <div class="dots" style="left:156px;top:22px;width:178px;height:96px"></div>
  <div class="ring"></div>
  <div class="photo" role="img" aria-label="Smiling man standing with colleagues in a bright office"></div>
  <div class="bubble"></div>
  <h2>About Us</h2>
  <div class="copy">
    <p>There are many variations of passages of Lorem Ipsum available, but the majority have suffered alteration in some form, by injected humour, or randomised words which don't look even slightly believable.</p>
    <p>There are many variations of passages of Lorem Ipsum available,</p>
  </div>
  <span class="btn" style="left:643px;top:318px">Read More</span>
</section>

<section class="schedule">
  <div class="photo-wash" role="img" aria-label="Office team background, tinted navy"></div>
  <h2>Choose A<br>Schedule</h2>
  <p>There are many variations of passages of Lorem Ipsum available, but the majority</p>
  <span class="btn">View Details</span>
  <div class="cal-bracket"></div>
  <div class="cal">
    <table>
      <tr><th class="title" colspan="7">MARCH 2022</th></tr>
      <tr><th class="day">Sun</th><th class="day">Mon</th><th class="day">Tue</th><th class="day">Wed</th><th class="day">Thu</th><th class="day">Fri</th><th class="day">Sat</th></tr>
      <tr><td class="mute">27</td><td class="mute">28</td><td>1</td><td>2</td><td>3</td><td>4</td><td>5</td></tr>
      <tr><td>6</td><td>7</td><td>8</td><td>9</td><td>10</td><td>11</td><td>12</td></tr>
      <tr><td>13</td><td>14</td><td>15</td><td>16</td><td>17</td><td>18</td><td>19</td></tr>
      <tr><td>20</td><td>21</td><td>22</td><td>23</td><td>24</td><td>25</td><td>26</td></tr>
      <tr><td>27</td><td>28</td><td>29</td><td>30</td><td>31</td><td class="mute">1</td><td class="mute">2</td></tr>
    </table>
  </div>
  <div class="cal-plus">+</div>
</section>

<section class="why">
  <div class="blob" style="left:-120px;top:40px;width:520px;height:480px"></div>
  <div class="blob" style="left:820px;top:-80px;width:480px;height:300px"></div>
  <h2>Why Choose Us</h2>
  <div class="dots" style="left:455px;top:174px;width:110px;height:40px;background-size:9px 9px;background-image:radial-gradient(circle,#333 1.3px,transparent 1.8px)"></div>
  <div class="dots" style="left:640px;top:435px;width:110px;height:40px;background-size:9px 9px;background-image:radial-gradient(circle,#333 1.3px,transparent 1.8px)"></div>
  <div class="center-ring"></div>
  <div class="center"></div>

  <div class="feature" style="left:160px;top:174px">
    <div class="frame"></div><div class="pill"></div>
    <div class="label"><b>TRUSTED</b><span>There are many variations</span></div>
    <div class="icon"><svg width="44" height="44" viewBox="0 0 44 44"><path d="M22 30 12 20a6 6 0 0 1 10-7 6 6 0 0 1 10 7z" fill="#ff6a00"/><path d="M4 24c4 0 8 10 14 14M40 24c-4 0-8 10-14 14" fill="none" stroke="#ff6a00" stroke-width="4" stroke-linecap="round"/></svg></div>
  </div>
  <div class="feature" style="left:160px;top:348px">
    <div class="frame"></div><div class="pill"></div>
    <div class="label"><b>SUPPORT</b><span>There are many variations</span></div>
    <div class="icon"><svg width="48" height="40" viewBox="0 0 48 40"><path d="M2 12h10l12 10 10-10h12v14H34L24 34 14 26H2z" fill="#ff6a00"/><path d="M16 18l8 6 8-6" fill="none" stroke="#fff" stroke-width="2"/></svg></div>
  </div>
  <div class="feature" style="left:756px;top:174px">
    <div class="frame" style="left:20px"></div><div class="pill"></div>
    <div class="label"><b>VALUED</b><span>There are many variations</span></div>
    <div class="icon"><svg width="44" height="44" viewBox="0 0 44 44"><path d="M8 16l6-8h16l6 8-14 20z" fill="#ff6a00"/><path d="M8 16h28M18 16l4 20 4-20" fill="none" stroke="#fff" stroke-width="1.5"/></svg></div>
  </div>
  <div class="feature" style="left:756px;top:348px">
    <div class="frame" style="left:20px"></div><div class="pill"></div>
    <div class="label"><b>MOTIVATE</b><span>There are many variations</span></div>
    <div class="icon"><svg width="40" height="44" viewBox="0 0 40 44"><path d="M20 4a14 14 0 0 0-8 25v7h16v-7A14 14 0 0 0 20 4z" fill="#ff6a00"/><rect x="14" y="38" width="12" height="4" fill="#ff6a00"/><path d="M20 26V12m-6 6 6-6 6 6" fill="none" stroke="#fff" stroke-width="2.5"/></svg></div>
  </div>
</section>

<section class="how">
  <div class="wash" role="img" aria-label="Colleagues working together, darkened"></div>
  <div class="orange-top"></div>
  <div class="orange-back"></div>
  <div class="video" role="img" aria-label="Video still of colleagues gathered around a laptop"></div>
  <div class="play"><svg width="36" height="40" viewBox="0 0 36 40"><path d="M2 2l32 18L2 38z" fill="#e81c1c"/></svg></div>
  <h2>How It Works</h2>
  <p>There are many variations of passages of Lorem Ipsum available, but the majority have suffered alteration in some form, by injected humour, or randomised words which don't look even slightly believable.</p>
  <span class="btn">Watch Video</span>
</section>

<section class="events">
  <div class="dots" style="left:0;top:2px;width:118px;height:64px"></div>
  <div class="dots" style="left:1087px;top:600px;width:113px;height:60px"></div>
  <h2>Events</h2>
  <div class="event-main" role="img" aria-label="Two women laughing during a meeting at a laptop"></div>
  <div class="abs" style="left:160px;top:424px;width:400px">
    <div class="date"><svg width="13" height="13" viewBox="0 0 13 13"><rect x=".5" y="1.5" width="12" height="11" fill="none" stroke="#222"/><path d="M.5 4.5h12" stroke="#222"/></svg>11.03.22</div>
    <div class="event-title" style="margin-top:8px">Lorem Ipsum is simply<br>dummy text</div>
    <p style="margin-top:8px;font-size:13px;line-height:23px">There are many variations of passages of Lorem Ipsum available, but the majority</p>
  </div>

  <div class="event-side" style="top:119px">
    <div class="thumb" role="img" aria-label="Team reviewing a tablet together" style="background:linear-gradient(135deg,#c7c3bd,#6f6860)"></div>
    <div class="info"><div class="date"><svg width="13" height="13" viewBox="0 0 13 13"><rect x=".5" y="1.5" width="12" height="11" fill="none" stroke="#222"/><path d="M.5 4.5h12" stroke="#222"/></svg>11.03.22</div><div class="event-title" style="margin-top:6px">Lorem Ipsum is simply<br>dummy text</div></div>
  </div>
  <div class="event-side" style="top:256px">
    <div class="thumb" role="img" aria-label="Team meeting around a conference table" style="background:linear-gradient(135deg,#b9b6b3,#4e4a4a)"></div>
    <div class="info"><div class="date"><svg width="13" height="13" viewBox="0 0 13 13"><rect x=".5" y="1.5" width="12" height="11" fill="none" stroke="#222"/><path d="M.5 4.5h12" stroke="#222"/></svg>11.03.22</div><div class="event-title" style="margin-top:6px">Lorem Ipsum is simply<br>dummy text</div></div>
  </div>
  <div class="event-side" style="top:395px">
    <div class="thumb" role="img" aria-label="Woman smiling at her desk" style="background:linear-gradient(135deg,#e6e3de,#7d756d)"></div>
    <div class="info"><div class="date"><svg width="13" height="13" viewBox="0 0 13 13"><rect x=".5" y="1.5" width="12" height="11" fill="none" stroke="#222"/><path d="M.5 4.5h12" stroke="#222"/></svg>11.03.22</div><div class="event-title" style="margin-top:6px">Lorem Ipsum is simply<br>dummy text</div></div>
  </div>
  <span class="btn">View All</span>
</section>

<section class="contact-sec">
  <div class="wash" role="img" aria-label="Group of coworkers, tinted orange"></div>
  <svg class="abs" style="left:0;top:0" width="1200" height="80" viewBox="0 0 1200 80">
    <path d="M0 0H1200V10C900 60 300 60 0 10Z" fill="#fff"/>
    <path d="M0 10C300 60 900 60 1200 10" fill="none" stroke="#15203a" stroke-width="6"/>
    <path d="M555 58a46 46 0 0 1 90 0" fill="#fff" stroke="#15203a" stroke-width="6"/>
  </svg>
  <h2>Contact Us</h2>
  <div class="field" style="left:371px;top:169px;width:226px">First Name</div>
  <div class="field" style="left:603px;top:169px;width:226px">Last Name</div>
  <div class="field" style="left:371px;top:221px;width:226px">Email Address</div>
  <div class="field" style="left:603px;top:221px;width:226px">Phone No</div>
  <div class="field" style="left:371px;top:272px;width:458px;height:112px">Message</div>
  <span class="btn submit">Submit Now</span>
</section>

<section class="testi">
  <h2>Testimonial</h2>
  <div class="quote" style="left:158px">
    <div class="stars"><svg width="90" height="16" viewBox="0 0 90 16"><g fill="#f5b400"><path id="st" d="M8 0l2.4 5 5.6.6-4.2 3.8 1.2 5.6L8 12.2 3 15l1.2-5.6L0 5.6 5.6 5z"/><use href="#st" x="18.5"/><use href="#st" x="37"/><use href="#st" x="55.5"/><use href="#st" x="74"/></g></svg><span class="line"></span></div>
    <div class="mark">&ldquo;</div>
    <p>There are many variations of passages of Lorem Ipsum available, but the majority have suffered alteration in some form, by injected humour, or randomised words which don't look even slightly believable. <span style="color:#bbb;font-family:Georgia,serif;font-size:26px">&rdquo;</span></p>
    <div class="who"><div class="tri"></div><div class="avatar" role="img" aria-label="Client portrait"></div><div class="name">Mark Ellis<br>Businessman , USA</div></div>
  </div>
  <div class="quote" style="left:459px">
    <div class="stars"><svg width="90" height="16" viewBox="0 0 90 16"><g fill="#f5b400"><use href="#st"/><use href="#st" x="18.5"/><use href="#st" x="37"/><use href="#st" x="55.5"/><use href="#st" x="74"/></g></svg><span class="line"></span></div>
    <div class="mark">&ldquo;</div>
    <p>There are many variations of passages of Lorem Ipsum available, but the majority have suffered alteration in some form, by injected humour, or randomised words which don't look even slightly believable. <span style="color:#bbb;font-family:Georgia,serif;font-size:26px">&rdquo;</span></p>
    <div class="who"><div class="tri"></div><div class="avatar" role="img" aria-label="Client portrait"></div><div class="name">Sam Porter<br>Businessman , USA</div></div>
  </div>
  <div class="quote" style="left:760px">
    <div class="stars"><svg width="90" height="16" viewBox="0 0 90 16"><g fill="#f5b400"><use href="#st"/><use href="#st" x="18.5"/><use href="#st" x="37"/><use href="#st" x="55.5"/><use href="#st" x="74"/></g></svg><span class="line"></span></div>
    <div class="mark">&ldquo;</div>
    <p>There are many variations of passages of Lorem Ipsum available, but the majority have suffered alteration in some form, by injected humour, or randomised words which don't look even slightly believable. <span style="color:#bbb;font-family:Georgia,serif;font-size:26px">&rdquo;</span></p>
    <div class="who"><div class="tri"></div><div class="avatar" role="img" aria-label="Client portrait"></div><div class="name">Mark Ellis<br>Businessman , USA</div></div>
  </div>
  <div class="pager"><i class="on"></i><i></i><i></i></div>
</section>

<footer class="footer">
  <div class="abs" style="left:158px;top:88px">
    <div class="logo">velquo</div>
    <p class="about-txt">There are many variations of passages of Lorem Ipsum available, but the majority have suffered alteration in some form, by injected humour, or randomised .</p>
  </div>
  <div class="col" style="left:400px;width:280px">
    <h4>Contact US</h4>
    <ul class="contact-list" style="margin-left:26px">
      <li><span class="ic-circle" style="background:#fff"><svg width="12" height="14" viewBox="0 0 12 14"><path d="M6 0a5 5 0 0 0-5 5c0 4 5 9 5 9s5-5 5-9a5 5 0 0 0-5-5z" fill="#ff6a00"/><circle cx="6" cy="5" r="1.8" fill="#fff"/></svg></span><span>One Harbor Plaza<br>2100 Linden Avenue Austin<br>TX, 73301</span></li>
      <li><span class="ic-circle" style="background:#fff"><svg width="14" height="10" viewBox="0 0 14 10"><rect x=".5" y=".5" width="13" height="9" fill="#ff6a00"/><path d="M.5 .5 7 6l6.5-5.5" fill="none" stroke="#fff"/></svg></span><span style="line-height:26px">info@velquo.com</span></li>
      <li><span class="ic-circle" style="background:#fff"><svg width="13" height="13" viewBox="0 0 24 24"><path fill="#ff6a00" d="M6.6 10.8a15 15 0 0 0 6.6 6.6l2.2-2.2c.3-.3.7-.4 1-.2 1.1.4 2.3.6 3.6.6.6 0 1 .4 1 1V20c0 .6-.4 1-1 1A17 17 0 0 1 3 4c0-.6.4-1 1-1h3.5c.6 0 1 .4 1 1 0 1.3.2 2.5.6 3.6.1.3 0 .7-.2 1z"/></svg></span><span style="line-height:26px">555-014-2870</span></li>
    </ul>
  </div>
  <div class="col" style="left:680px;width:204px">
    <h4>Company</h4>
    <ul style="margin-left:44px">
      <li><span>&rarr;</span>Home</li><li><span>&rarr;</span>About</li><li><span>&rarr;</span>Solution</li><li><span>&rarr;</span>Event</li><li><span>&rarr;</span>Contact Us</li>
    </ul>
  </div>
  <div class="col" style="left:884px;width:200px">
    <h4>Follow Us</h4>
    <ul class="social" style="margin-left:50px;margin-top:14px">
      <li><span class="sq"></span>Friendhub</li><li><span class="sq"></span>Chirper</li><li><span class="sq"></span>Workline</li><li><span class="sq"></span>Photogrid</li><li><span class="sq"></span>Clipstream</li>
    </ul>
  </div>
  <div class="copy">Copyright©2022 <b>velquo</b> , All Rights Reserved.</div>
</footer>

</body>
</html>
```